Business Card *

A business card design
Use the logo uploaded in the brief page.
You may use placeholders in your design layouts.
I will provide the actual business card details to the winning designer.

Logo
Place for contact info (name, title, phone, email, etc)

Requirements
Must have
• Logo

```html
<!DOCTYPE html>
<html lang="en">
<head>
<meta charset="utf-8">
<title>Harrowfield Business Card</title>
<link href="https://fonts.googleapis.com/css2?family=Poppins:wght@400;500;700;800&display=swap" rel="stylesheet">
<style>
  :root {
    --stage: #1b1c1e;
    --card: #23272a;
    --card-edge: #2c3033;
    --silver: #a7a9ab;
    --silver-light: #c9cacb;
    --green: #3dbb3f;
    --green-light: #8ed14f;
    --text: #c4c6c8;
  }
  * { margin: 0; padding: 0; box-sizing: border-box; }
  html, body { width: 1200px; height: 800px; overflow: hidden; }
  body {
    background: var(--stage);
    font-family: "Poppins", sans-serif;
    display: flex;
    align-items: center;
    justify-content: center;
    gap: 48px;
  }
  .card {
    width: 540px;
    height: 310px;
    background: var(--card);
    border-radius: 18px;
    border: 1px solid var(--card-edge);
    position: relative;
    box-shadow: 0 18px 40px rgba(0,0,0,0.45);
  }
  .card--front {
    display: flex;
    align-items: center;
    justify-content: center;
  }
  .brand {
    display: flex;
    align-items: center;
    gap: 14px;
  }
  .brand__mark {
    width: 46px; height: 46px;
    border-radius: 50%;
    background: var(--silver);
  }
  .brand__name {
    font-weight: 800;
    font-size: 38px;
    letter-spacing: 1px;
    color: var(--silver-light);
  }
  .card--back { padding: 44px 40px; }
  .back__brand {
    position: absolute;
    right: 40px; top: 50%;
    transform: translateY(-50%);
    display: flex;
    flex-direction: column;
    align-items: center;
    gap: 12px;
  }
  .back__brand .brand__mark {
    width: 92px; height: 92px;
    background: var(--green);
  }
  .back__brand .brand__name { font-size: 18px; color: var(--silver); }
  .details__company {
    font-weight: 800;
    font-size: 24px;
    color: var(--silver);
    line-height: 1.1;
  }
  .details__tagline {
    font-weight: 700;
    font-size: 9px;
    letter-spacing: 1px;
    color: var(--green);
    margin-bottom: 18px;
  }
  .details__person {
    font-weight: 500;
    font-size: 16px;
    color: var(--text);
    line-height: 1.2;
  }
  .details__role {
    font-size: 12px;
    color: var(--green);
    margin-bottom: 16px;
  }
  .details__address {
    font-size: 11px;
    color: var(--text);
    line-height: 1.5;
    margin-bottom: 12px;
  }
  .contact { list-style: none; }
  .contact__item {
    display: flex;
    align-items: center;
    gap: 8px;
    font-size: 11px;
    color: var(--text);
    line-height: 1.8;
  }
  .contact__item svg { width: 14px; height: 14px; flex: none; }
  .contact__accent { color: var(--green); }
</style>
</head>
<body>
  <section class="card card--front" aria-label="Card front">
    <div class="brand">
      <span class="brand__mark"></span>
      <span class="brand__name">HARROWFIELD</span>
    </div>
  </section>

  <section class="card card--back" aria-label="Card back">
    <div class="details">
      <p class="details__company">HARROWFIELD</p>
      <p class="details__tagline">AGRICULTURE AND INDUSTRY</p>
      <p class="details__person">LENA R. CORWIN</p>
      <p class="details__role">Executive Director</p>
      <p class="details__address">PO BOX 418 Mill Lane<br>4th street Ashford,USA</p>
      <ul class="contact">
        <li class="contact__item">
          <svg viewBox="0 0 16 16" fill="none" stroke="#3dbb3f" stroke-width="1.4"><circle cx="8" cy="8" r="7"/><path d="M5.5 4.5l1.5 1.5-1 1c.6 1.3 1.6 2.3 2.9 2.9l1-1 1.6 1.5-1 1.1C7.6 11.3 4.7 8.4 4.5 5.5z" fill="#3dbb3f" stroke="none"/></svg>
          555-014-2260
        </li>
        <li class="contact__item">
          <svg viewBox="0 0 16 16" fill="none" stroke="#3dbb3f" stroke-width="1.4"><circle cx="8" cy="8" r="7"/><rect x="4.5" y="5.5" width="7" height="5" fill="#3dbb3f" stroke="none"/><path d="M4.5 5.8L8 8.4l3.5-2.6" stroke="#23272a" stroke-width="0.9"/></svg>
          info@harrowfield.com
        </li>
        <li class="contact__item">
          <svg viewBox="0 0 16 16" fill="none" stroke="#3dbb3f" stroke-width="1.2"><circle cx="8" cy="8" r="7"/><circle cx="8" cy="8" r="3.6"/><path d="M4.4 8h7.2M8 4.4c-1.4 2.2-1.4 5 0 7.2M8 4.4c1.4 2.2 1.4 5 0 7.2"/></svg>
          <span>www.<span class="contact__accent">harrowfield</span>.com</span>
        </li>
      </ul>
    </div>
    <div class="back__brand">
      <span class="brand__mark"></span>
      <span class="brand__name">HARROWFIELD</span>
    </div>
  </section>
</body>
</html>
```